Design a Website in Wordpress for an Australian Health Training Company in Health related courses

We require a WORDPRESS based Website (due to add on's we need to use for third party software) to replace our old site.
We offer national face to face delivery in medical reception, terminology and also administration.
The website will have around 6 pages and the ability to describe our main 6 courses (perhaps on the Courses page this may be tabs opening up to details for example?)
I have attached a previous sample of a Joomla site which was being developed (please do not feel you have to copy this - but I am just giving it as a sample - copying would be boring). But it gives an idea of look/feel and colours which may be suitable. Open to other ideas though.
I will provide some of the content, but would like the ability to finish the content myself.
Images and graphics are important. While a few medical photos re great - don't be tempted to us all pictures of doctors and nurses (although a couple would be good) - these are administrative courses so general corporate, eye catching visionary pictures of people in general are great. A medical type picture is also fine.
THE BOOKING system - will be via an ADD ON which will occur at the end of the project and is supplied by a third party software company (our student management system). This project will include up to 2 hours working with the Tech guys from the third party software to enable the ADD ON. If this ADD ON requires more time, we will pay hourly (although I do not expect it will).
Mostly a female market, many mature aged women target 25-45 yrs. Mixture of medical/health and corporate. Maybe a bit of mums returning to work and corporate inspiration.
It Company
Coded - Design and coding required
5+ page
Must have
- Wordpress
- Great graphics
- Interesting
- professional and clean
- Enquiry section (info Pak)
- Should have a University feel to it - Education
- Pages
- Home Page - About Us - Recruitment -Courses - Class Schedule - Traineeships Queensland Funding - Latest News Blog - Corporate Training- Contact us

```html
<!DOCTYPE html>
<html lang="en">
<head>
<meta charset="utf-8">
<title>Harbourline Institute Of Training</title>
<link href="https://fonts.googleapis.com/css2?family=Open+Sans:wght@400;600;700&family=Roboto:wght@300;400;500;700&display=swap" rel="stylesheet">
<style>
:root{
  --blue:#0a4d9e;
  --blue-dark:#083d7d;
  --orange:#f5a13a;
  --text:#4a4a4a;
  --muted:#777;
  --line:#dcdce3;
  --panel:#f0f0f5;
  --white:#fff;
}
*{box-sizing:border-box;margin:0;padding:0}
html,body{width:1200px;height:2675px;overflow:hidden;background:var(--white)}
body{font-family:"Open Sans",Arial,sans-serif;color:var(--text);font-size:13px;position:relative}
.abs{position:absolute}
.section{position:absolute;left:0;width:1200px}
h2.title{font-family:"Roboto",Arial,sans-serif;font-weight:300;font-size:23px;color:#333;position:absolute}
h2.title::after{content:"";position:absolute;left:0;bottom:-9px;width:30px;height:2px;background:var(--blue)}
h2.title.center::after{left:50%;margin-left:-15px}
.dot{display:inline-block;width:11px;height:11px;border-radius:50%;background:currentColor}

/* top bar */
.topbar{top:0;height:40px;background:var(--blue);color:var(--white);font-size:12px}
.topbar .item{position:absolute;top:12px;display:flex;align-items:center;gap:7px}
.topbar .socials{position:absolute;left:803px;top:14px;display:flex;gap:17px;opacity:.9}

/* header */
.header{top:40px;height:97px;background:var(--white)}
.logo{position:absolute;left:89px;top:12px;width:90px;text-align:center;font-family:"Roboto",sans-serif;font-weight:500;font-size:9px;line-height:1.25;color:var(--blue);text-transform:uppercase}
.logo .mark{display:block;width:34px;height:34px;background:var(--blue);margin:6px auto 0}
.nav{position:absolute;top:42px;left:0;font-size:12.5px;color:#333}
.nav a{position:absolute;white-space:nowrap;color:#333;text-decoration:none}
.nav a.active{color:var(--orange)}
.nav a.active::after{content:"";position:absolute;left:-6px;right:-6px;top:28px;height:2px;background:var(--orange)}
.btn-side{position:absolute;left:972px;width:139px;height:34px;color:var(--white);font-weight:700;font-size:12.5px;display:flex;align-items:center}
.btn-side .ic{width:34px;height:100%;display:flex;align-items:center;justify-content:center;border-right:1px solid rgba(255,255,255,.35)}
.btn-side span.lbl{flex:1;text-align:center}
.btn-enroll{top:13px;background:var(--orange)}
.btn-info{top:53px;background:var(--blue)}

/* hero */
.hero{top:137px;height:418px}
.hero .photo{position:absolute;inset:0;background:linear-gradient(100deg,#c9ccd2 0%,#e4e7ea 40%,#d5dbe1 62%,#a9b4bf 100%)}
.hero .panel{position:absolute;left:0;top:77px;width:526px;height:262px;background:rgba(255,255,255,.78)}
.hero h1{position:absolute;left:89px;top:124px;font-family:"Roboto",sans-serif;font-weight:400;font-size:27px;color:var(--blue)}
.hero h1 em{font-style:normal;color:var(--orange)}
.hero h1::after{content:"";position:absolute;left:0;bottom:-7px;width:30px;height:2px;background:var(--blue)}
.hero p{position:absolute;left:89px;top:175px;width:400px;font-size:12.5px;line-height:1.75;color:#444}
.btn-blue{position:absolute;background:var(--blue);color:var(--white);font-size:12.5px;display:flex;align-items:center;justify-content:center;gap:8px}
.btn-outline{position:absolute;border:1px solid var(--orange);color:var(--orange);font-size:12.5px;display:flex;align-items:center;justify-content:center;gap:8px}

/* about */
.about{top:555px;height:340px}
.about p{position:absolute;left:89px;width:630px;font-size:12.5px;line-height:1.8;color:#555}
.about .frame{position:absolute;left:842px;top:87px;width:269px;height:219px;border:4px solid var(--line)}
.about .photo{position:absolute;left:761px;top:37px;width:327px;height:228px;background:linear-gradient(135deg,#7e93a8,#2f4660 55%,#1e2e44)}

/* courses */
.courses{top:895px;height:330px;background:var(--panel)}
.course{position:absolute;top:98px;width:241px;height:182px;background:var(--white);border:1px solid var(--line);text-align:center}
.course .icon{position:absolute;left:50%;top:-30px;margin-left:-31px;width:62px;height:62px;border-radius:50%;background:var(--white);border:1px solid var(--line);display:flex;align-items:center;justify-content:center}
.course .icon i{display:block;width:38px;height:38px;border-radius:50%}
.course h3{margin-top:55px;font-family:"Roboto",sans-serif;font-weight:500;font-size:13px;color:#222}
.course h3::after{content:"";display:block;width:36px;height:2px;background:var(--orange);margin:9px auto 0}
.course p{margin:12px auto 0;width:195px;font-size:12.5px;line-height:1.5;color:#666}
.course a{display:block;margin-top:9px;font-size:12.5px;font-weight:600;color:var(--blue)}
.course a.hl{color:var(--orange)}
.pager{position:absolute;top:305px;left:590px;display:flex;gap:4px}
.pager i{width:8px;height:8px;border-radius:50%;background:#c8c8d0}
.pager i.on{background:var(--orange)}

/* why + form */
.why{top:1225px;height:401px}
.acc{position:absolute;left:89px;width:551px;height:40px;border:1px solid var(--line);display:flex;align-items:center;padding-left:13px;gap:12px;font-size:13px;color:#444}
.acc .tri{width:0;height:0;border-top:4px solid transparent;border-bottom:4px solid transparent;border-left:6px solid var(--orange)}
.acc.open{background:var(--blue);color:var(--white);border-color:var(--blue)}
.acc.open .tri{border-left:4px solid transparent;border-right:4px solid transparent;border-top:6px solid var(--white);border-bottom:0}
.acc-body{position:absolute;left:89px;top:261px;width:551px;height:58px;border:1px solid var(--line);border-top:0;padding:8px 20px;font-size:12px;line-height:1.75;color:#555}
.field{position:absolute;left:667px;width:444px;height:40px;border-bottom:1px solid var(--line);display:flex;align-items:center;gap:12px;font-size:12.5px;color:#777}
.field .ic{width:14px;display:flex;justify-content:center}
.field .caret{margin-left:auto;width:0;height:0;border-left:3px solid transparent;border-right:3px solid transparent;border-top:4px solid #555}

/* posts */
.posts{top:1626px;height:523px;background:var(--panel)}
.posts .rule{position:absolute;left:0;top:116px;width:1200px;height:1px;background:#cfd0d8}
.post{position:absolute;top:168px;width:241px;height:319px;background:var(--white);border:1px solid var(--line)}
.date{position:absolute;top:84px;width:85px;height:62px;background:var(--white);border:1px solid var(--line);display:flex;align-items:center;justify-content:center;gap:6px}
.date b{font-family:"Roboto",sans-serif;font-weight:500;font-size:30px;color:var(--orange)}
.date span{font-size:11px;line-height:1.15;color:#777}
.date::after{content:"";position:absolute;left:50%;bottom:-8px;margin-left:-7px;border-left:7px solid transparent;border-right:7px solid transparent;border-top:8px solid var(--white)}
.date.active{background:var(--blue);border-color:var(--blue)}
.date.active b,.date.active span{color:var(--white)}
.date.active::after{border-top-color:var(--blue)}
.post .photo{height:169px}
.post h4{margin:14px 14px 0;font-family:"Roboto",sans-serif;font-weight:500;font-size:14px;color:#222}
.post p{margin:10px 14px 0;font-size:12.5px;line-height:1.5;color:#666}
.post .more{position:absolute;left:14px;top:278px;font-size:12.5px;font-weight:600;color:var(--blue);display:flex;gap:6px;align-items:center}
.post .bubble{position:absolute;right:18px;top:268px;width:36px;height:36px;border-radius:50%;background:#ececf1;display:flex;align-items:center;justify-content:center}
.post .bubble em{position:absolute;right:-6px;top:-8px;width:18px;height:18px;border-radius:50%;background:var(--blue);color:var(--white);font-style:normal;font-size:10px;display:flex;align-items:center;justify-content:center}

/* testimonials */
.testi{top:2149px;height:262px}
.testi .who{position:absolute;left:560px;top:65px;width:80px;text-align:center;font-size:12.5px;color:#333}
.testi .who b{display:block;font-family:"Roboto",sans-serif;font-size:26px;line-height:.8;color:#333}
.testi .quote{position:absolute;left:94px;top:128px;width:1012px;height:103px;border:1px solid var(--line);padding:14px 36px;text-align:center;font-size:12.5px;line-height:1.8;color:#555}
.testi .quote::before{content:"";position:absolute;left:50%;top:-8px;margin-left:-8px;width:14px;height:14px;background:var(--white);border-left:1px solid var(--line);border-top:1px solid var(--line);transform:rotate(45deg)}

/* footer */
.footer{top:2411px;height:224px;background:var(--blue);color:var(--white)}
.footer h5{position:absolute;top:30px;font-family:"Roboto",sans-serif;font-weight:700;font-size:15px;text-transform:uppercase}
.footer h5::after{content:"";position:absolute;left:0;bottom:-7px;width:30px;height:2px;background:var(--orange)}
.footer .copy{position:absolute;left:89px;top:66px;width:310px;font-size:12.5px;line-height:1.6}
.tweet{position:absolute;left:449px;width:330px;display:flex;gap:10px;font-size:12px;line-height:1.45}
.tweet a{color:var(--orange)}
.contact{position:absolute;left:809px;display:flex;gap:12px;align-items:center;font-size:12px}
.subscribe{position:absolute;left:809px;top:160px;width:302px;height:38px;display:flex}
.subscribe .input{flex:1;background:#1c5fae;font-size:12px;display:flex;align-items:center;padding-left:14px;color:#dbe6f5}
.subscribe .go{width:44px;background:var(--orange);display:flex;align-items:center;justify-content:center}
.bottombar{top:2635px;height:40px;background:var(--blue-dark);color:var(--white);font-size:11px}
.bottombar .c{position:absolute;left:89px;top:13px}
.bottombar .c b{color:var(--orange);font-weight:400}
.bottombar .socials{position:absolute;left:955px;top:15px;display:flex;gap:19px;opacity:.9}
</style>
</head>
<body>

<!-- top bar -->
<div class="section topbar">
  <div class="item" style="left:103px">
    <svg width="13" height="13" viewBox="0 0 14 14"><circle cx="7" cy="7" r="6" fill="var(--orange)"/><path d="M1 7h12M7 1c-3 3-3 9 0 12M7 1c3 3 3 9 0 12" stroke="var(--blue)" fill="none" stroke-width="1"/></svg>
    English <svg width="7" height="5"><path d="M0 0h7L3.5 5z" fill="#fff"/></svg>
  </div>
  <div class="item" style="left:209px">
    <svg width="10" height="13" viewBox="0 0 10 14"><path d="M5 0a5 5 0 0 1 5 5c0 4-5 9-5 9S0 9 0 5a5 5 0 0 1 5-5z" fill="var(--orange)"/><circle cx="5" cy="5" r="2" fill="var(--blue)"/></svg>
    40215, Carlton, Merriweather St. LTD
  </div>
  <div class="socials"><i class="dot"></i><i class="dot"></i><i class="dot"></i><i class="dot"></i><i class="dot"></i><i class="dot"></i></div>
  <div class="item" style="left:1005px"><i class="dot"></i> Chat name</div>
</div>

<!-- header -->
<div class="section header">
  <div class="logo">Harbourline Institute of Training<i class="mark"></i></div>
  <nav class="nav">
    <a class="active" style="left:237px">About us</a>
    <a style="left:326px">Our Courses</a>
    <a style="left:437px">Class Schedule</a>
    <a style="left:562px">RPL</a>
    <a style="left:619px">Latest News</a>
    <a style="left:726px">Corporate Training</a>
    <a style="left:874px">Contact Us</a>
  </nav>
  <div class="btn-side btn-enroll">
    <span class="ic"><svg width="14" height="14" viewBox="0 0 14 14"><path d="M4 13V5a1.3 1.3 0 0 1 2.6 0v3h3.4a2 2 0 0 1 2 2v3z" fill="#fff"/></svg></span>
    <span class="lbl">Enroll Now</span>
  </div>
  <div class="btn-side btn-info">
    <span class="ic" style="font-size:15px">!</span>
    <span class="lbl">Info Pack</span>
  </div>
</div>

<!-- hero -->
<div class="section hero">
  <div class="photo" role="img" aria-label="Trainer presenting at a flipchart to a seated group of professionals"></div>
  <div class="panel"></div>
  <h1>Courses for <em>Busy People</em></h1>
  <p>Our unique quick CAT ( Combined Assessment &amp; Training ) class format delivers accelerated training that's specifically targeted at busy professionals...</p>
  <div class="btn-blue" style="left:89px;top:255px;width:129px;height:36px">Read More <svg width="12" height="8"><path d="M0 4h11M8 1l3 3-3 3" stroke="#fff" fill="none"/></svg></div>
</div>

<!-- about -->
<div class="section about">
  <h2 class="title" style="left:89px;top:33px">Harbourline Institute Of Training</h2>
  <p style="top:80px">Harbourline is Australia's Leading Provider of Educational, Training and Support Services for the Medical and Dental industry -  enabling students to be immediately skilled and 'job Ready' for a career in Health.</p>
  <p style="top:145px">Harbourline is a Registered Training Organisation offering specialised Medical Administration Training in over 15 locations Australia wide.  Harbourline have trained thousands of students the required knowledge and skills to become successful health care administrators.</p>
  <p style="top:210px">Our unique Short Medical Reception and Terminology Course and our Full Qualification is Nationally Accredited and the go-to recognised qualification in industry.</p>
  <div class="btn-outline" style="left:89px;top:271px;width:129px;height:35px">Read More <svg width="12" height="8"><path d="M0 4h11M8 1l3 3-3 3" stroke="var(--orange)" fill="none"/></svg></div>
  <div class="frame"></div>
  <div class="photo" role="img" aria-label="Colleagues working together at a laptop in a meeting"></div>
</div>

<!-- courses -->
<div class="section courses">
  <h2 class="title center" style="left:0;width:1200px;text-align:center;top:24px">Courses</h2>
  <div class="course" style="left:96px">
    <div class="icon"><i role="img" aria-label="Medical receptionist icon" style="background:#8fb3d9"></i></div>
    <h3>Medical Reception &amp; Terminology</h3>
    <p>Vivamus elementum semper nisi aenean vulputate eleifend tellus aenean leo ligula porttitor.</p>
    <a>Learn More</a>
  </div>
  <div class="course" style="left:352px">
    <div class="icon"><i role="img" aria-label="Business administration icon" style="background:#f2b36a"></i></div>
    <h3>Cert III Business Administration</h3>
    <p>Vivamus elementum semper nisi aenean vulputate eleifend tellus aenean leo ligula porttitor.</p>
    <a class="hl">Learn More</a>
  </div>
  <div class="course" style="left:608px">
    <div class="icon"><i role="img" aria-label="Keyboard icon" style="background:#b8bcc6"></i></div>
    <h3>Keyboard and Typing</h3>
    <p>Vivamus elementum semper nisi aenean vulputate eleifend tellus aenean leo ligula porttitor.</p>
    <a>Learn More</a>
  </div>
  <div class="course" style="left:865px">
    <div class="icon"><i role="img" aria-label="Online learning laptop icon" style="background:#f4c95a"></i></div>
    <h3>Harbourline Online</h3>
    <p>Vivamus elementum semper nisi aenean vulputate eleifend tellus aenean leo ligula porttitor.</p>
    <a>Learn More</a>
  </div>
  <div class="pager"><i class="on"></i><i></i></div>
</div>

<!-- why + info pack -->
<div class="section why">
  <h2 class="title" style="left:89px;top:50px">Why Harbourline Institute ?</h2>
  <div class="acc" style="top:87px"><i class="tri"></i>Quality</div>
  <div class="acc" style="top:131px"><i class="tri"></i>Experience</div>
  <div class="acc" style="top:176px"><i class="tri"></i>Value</div>
  <div class="acc open" style="top:221px"><i class="tri"></i>Industry Recognised</div>
  <div class="acc-body">Harbourline work hand in hand with industry to develop our core programme and consolidate the programme annually to keep the programme fresh and relevant.</div>
  <div class="acc" style="top:324px"><i class="tri"></i>Great Job Results</div>

  <h2 class="title" style="left:667px;top:50px">Email me an Info Pack</h2>
  <div class="field" style="top:90px"><span class="ic"><svg width="11" height="12"><circle cx="5.5" cy="3.5" r="3" fill="#888"/><path d="M0 12c0-4 11-4 11 0z" fill="#888"/></svg></span>Name</div>
  <div class="field" style="top:134px"><span class="ic"><svg width="12" height="9"><rect width="12" height="9" fill="#888"/><path d="M0 0l6 5 6-5" stroke="#fff" fill="none"/></svg></span>Email</div>
  <div class="field" style="top:179px"><span class="ic"><svg width="12" height="10"><path d="M0 1h2M4 1h8M0 5h2M4 5h8M0 9h2M4 9h8" stroke="#888"/></svg></span>Course<i class="caret"></i></div>
  <div class="field" style="top:223px"><span class="ic"><svg width="12" height="11"><path d="M0 2l4-2 4 2 4-2v9l-4 2-4-2-4 2z" fill="#888"/></svg></span>State<i class="caret"></i></div>
  <div class="field" style="top:268px"><span class="ic"><svg width="8" height="12"><rect width="8" height="12" rx="1" fill="#888"/><rect x="1.5" y="1.5" width="5" height="7" fill="#fff"/></svg></span>Mobile</div>
  <div class="btn-outline" style="left:667px;top:324px;width:444px;height:40px">Submit</div>
</div>

<!-- recent posts -->
<div class="section posts">
  <h2 class="title" style="left:89px;top:34px">Recent Posts</h2>
  <div class="rule"></div>

  <div class="date" style="left:94px"><b>27</b><span>Aug<br>2014</span></div>
  <div class="date active" style="left:353px"><b>27</b><span>Aug<br>2014</span></div>
  <div class="date" style="left:610px"><b>27</b><span>Aug<br>2014</span></div>
  <div class="date" style="left:868px"><b>27</b><span>Aug<br>2014</span></div>

  <article class="post" style="left:94px">
    <div class="photo" role="img" aria-label="Presenter leading a meeting at a whiteboard" style="background:linear-gradient(135deg,#dfe3e8,#9aa7b5)"></div>
    <h4>Student Greek Life Team</h4>
    <p>Vivamus elementum semper nisi aenean vulputate eleifend tellus aenean leo ligula porttitor eu.</p>
    <div class="more">Read More <svg width="12" height="8"><path d="M0 4h11M8 1l3 3-3 3" stroke="var(--blue)" fill="none"/></svg></div>
    <div class="bubble"><svg width="14" height="12"><path d="M1 1h12v8H5l-3 3V9H1z" fill="none" stroke="#999"/></svg><em>0</em></div>
  </article>
  <article class="post" style="left:353px">
    <div class="photo" role="img" aria-label="Hand writing training keywords on a dark board" style="background:linear-gradient(135deg,#40566b,#1f2f40)"></div>
    <h4>Form a new student ORG</h4>
    <p>Vivamus elementum semper nisi aenean vulputate eleifend tellus aenean leo ligula porttitor eu.</p>
    <div class="more">Read More <svg width="12" height="8"><path d="M0 4h11M8 1l3 3-3 3" stroke="var(--blue)" fill="none"/></svg></div>
    <div class="bubble"><svg width="14" height="12"><path d="M1 1h12v8H5l-3 3V9H1z" fill="none" stroke="#999"/></svg><em>0</em></div>
  </article>
  <article class="post" style="left:610px">
    <div class="photo" role="img" aria-label="Hand sketching a light bulb idea on a dark surface" style="background:linear-gradient(135deg,#27303a,#0d1218)"></div>
    <h4>Manage your organization</h4>
    <p>Vivamus elementum semper nisi aenean vulputate eleifend tellus aenean leo ligula porttitor eu.</p>
    <div class="more">Read More <svg width="12" height="8"><path d="M0 4h11M8 1l3 3-3 3" stroke="var(--blue)" fill="none"/></svg></div>
    <div class="bubble"><svg width="14" height="12"><path d="M1 1h12v8H5l-3 3V9H1z" fill="none" stroke="#999"/></svg><em>0</em></div>
  </article>
  <article class="post" style="left:868px">
    <div class="photo" role="img" aria-label="Audience raising hands at a conference" style="background:linear-gradient(135deg,#6a5a4c,#2c241e)"></div>
    <h4>Getting involved</h4>
    <p>Vivamus elementum semper nisi aenean vulputate eleifend tellus aenean leo ligula porttitor eu.</p>
    <div class="more">Read More <svg width="12" height="8"><path d="M0 4h11M8 1l3 3-3 3" stroke="var(--blue)" fill="none"/></svg></div>
    <div class="bubble"><svg width="14" height="12"><path d="M1 1h12v8H5l-3 3V9H1z" fill="none" stroke="#999"/></svg><em>0</em></div>
  </article>
</div>

<!-- testimonials -->
<div class="section testi">
  <h2 class="title center" style="left:0;width:1200px;text-align:center;top:18px">Testimonials</h2>
  <svg class="abs" style="left:520px;top:71px" width="9" height="14"><path d="M8 1L2 7l6 6" stroke="#bbb" stroke-width="2" fill="none"/></svg>
  <div class="who"><b>&ldquo;</b>Clara Hughes</div>
  <svg class="abs" style="left:672px;top:71px" width="9" height="14"><path d="M1 1l6 6-6 6" stroke="var(--blue)" stroke-width="2" fill="none"/></svg>
  <div class="quote">I completed the course on Feb 13th. Loved it. The trainers, Megan and Rosa were excellent in their delivery and knowledge. I want to say a huge thank you for the course and knowledge I came away with. I have secured a fantastic job after my first application! Such good value for money too! I would highly recommend it. I'm a mature age person so it's never too late to up -skill yourself to get what you deserve!</div>
</div>

<!-- footer -->
<footer class="section footer">
  <h5 style="left:89px">Harbourline Institute of Training</h5>
  <p class="copy">Quisque rutrum aenean imperdiet etiam ultricies nisi vel augue curabitur ullamcorper ultricies nisi nam eget dui etiam rhoncus maecenas tempus tellus eget condimentum rhoncus sem quam semper libero sit amet adipiscing sem neque ipsum. lorem ipsum dolor sit amet.</p>

  <h5 style="left:449px">JV Updates</h5>
  <div class="tweet" style="top:66px"><i class="dot" style="color:var(--orange);width:9px;height:9px;margin-top:4px;flex:none"></i><div>Be yourself; everyone else is already taken.<br>-Dorothy Lane <a>#planyourday</a><br>lnk.example/4TQ2</div></div>
  <div style="position:absolute;left:449px;top:136px;width:330px;height:1px;background:rgba(255,255,255,.3)"></div>
  <div class="tweet" style="top:146px"><i class="dot" style="color:var(--orange);width:9px;height:9px;margin-top:4px;flex:none"></i><div>Free Phone Six Mockup Dock - Mockup Premium PSD Mockups, Free PSD Mockups, Real Photo Mockups <a>mockupshelf.example/free-phone-6...</a></div></div>

  <h5 style="left:809px">Contact &amp; Subscribe</h5>
  <div class="contact" style="top:68px"><svg width="10" height="13" viewBox="0 0 10 14"><path d="M5 0a5 5 0 0 1 5 5c0 4-5 9-5 9S0 9 0 5a5 5 0 0 1 5-5z" fill="var(--orange)"/></svg>Box 48210 Kestrel Lane, Brookvale 2100</div>
  <div class="contact" style="top:97px"><svg width="11" height="11" viewBox="0 0 12 12"><path d="M2 0l3 3-1.5 1.5a7 7 0 0 0 4 4L9 7l3 3-2 2C5 12 0 7 0 2z" fill="var(--orange)"/></svg>Phone: + 61 (02) 55501874</div>
  <div class="contact" style="top:125px"><svg width="12" height="11"><rect y="3" width="12" height="6" fill="var(--orange)"/><rect x="3" width="6" height="3" fill="var(--orange)"/><rect x="3" y="8" width="6" height="3" fill="#fff" stroke="var(--orange)"/></svg>Fax: + 61 (02) 55501874</div>
  <div class="subscribe"><div class="input">Enter email address...</div><div class="go"><svg width="16" height="14"><path d="M0 6L16 0 12 14 8 9z" fill="#fff"/></svg></div></div>
</footer>

<div class="section bottombar">
  <div class="c">&copy; <b>2016</b> Harbourline Institute Of Training.</div>
  <div class="socials"><i class="dot" style="width:9px;height:9px"></i><i class="dot" style="width:9px;height:9px"></i><i class="dot" style="width:9px;height:9px"></i><i class="dot" style="width:9px;height:9px"></i><i class="dot" style="width:9px;height:9px"></i><i class="dot" style="width:9px;height:9px"></i></div>
</div>

</body>
</html>
```